General Power Point Presentation Pack

Hello Designers,

I am after a professional looking Microsoft PowerPoint deck that can be used for our corporate presentations. The pack should include a:

Title Page
Tittle and Content Page
Section Header Sheet
Two Content Page
Title Only Page
Blank Page
Content with Caption Page
Picture with Caption Page

I have included my brand guidelines and colours. I have also included some photos you may be able to use. Can you please ensure the pack has page numbering and that when you print it that it can be printed to full A4 Page.

Industry/Entity Type

Property Development & Construction

Requirements
Must have
• Prefer a white or very light coloured background

```html
<!DOCTYPE html>
<html lang="en">
<head>
<meta charset="utf-8">
<title>Stoneway Presentation Pack</title>
<link href="https://fonts.googleapis.com/css2?family=Roboto+Condensed:wght@400;700&family=Roboto:wght@400;500;700&display=swap" rel="stylesheet">
<style>
:root{
  --orange:#d2622a;
  --orange-light:#e9925f;
  --orange-pale:#f4c4a3;
  --cream:#f4ebdd;
  --tan:#c8ab86;
  --grey:#75766f;
  --slate:#62655f;
  --sage:#7fa79a;
  --ink:#3a3a38;
  --muted:#8b8b86;
  --canvas:#ececea;
  --white:#ffffff;
}
*{box-sizing:border-box;margin:0;padding:0}
html,body{width:1200px;height:3148px;overflow:hidden}
body{background:var(--canvas);font-family:"Roboto",Arial,sans-serif;color:var(--ink);position:relative}
.slide{position:absolute;width:360px;height:290px;background:var(--white);overflow:hidden;box-shadow:0 4px 14px rgba(0,0,0,.12)}
.head{font-family:"Roboto Condensed","Arial Narrow",sans-serif;font-weight:700;text-transform:uppercase;letter-spacing:.3px}
.photo{position:absolute}
.photo-glass{background:linear-gradient(135deg,#e9b48f 0%,#c96a36 45%,#f0d2ba 100%)}
.photo-interior{background:linear-gradient(160deg,#ded6c9 0%,#bfb3a0 50%,#8d8676 100%)}
.photo-building{background:linear-gradient(170deg,#c9d8df 0%,#a9a294 55%,#6f6a5e 100%)}
.photo-tower{background:linear-gradient(170deg,#d8e3e6 0%,#b9b4a8 55%,#7c776c 100%)}
.photo-lobby{background:linear-gradient(160deg,#d9cbb3 0%,#a99479 100%)}
.brand{display:flex;align-items:center;gap:4px;font-family:"Roboto",Arial,sans-serif;font-weight:700;font-size:10px;color:var(--orange);position:absolute}
.brand::before{content:"";width:7px;height:7px;background:currentColor}
.brand.light{color:var(--white)}
.foot{position:absolute;left:18px;right:18px;bottom:10px;display:flex;justify-content:space-between;align-items:center}
.foot .brand{position:static;font-size:8px}
.foot small{font-size:5px;color:var(--muted)}
.s-title{position:absolute;left:18px;top:16px;font-size:15px;color:var(--orange)}
.lorem-head{font-size:7px;font-weight:700;color:var(--ink);margin-bottom:3px}
.copy{font-size:5px;line-height:1.55;color:var(--muted)}
.bullets{list-style:none;font-size:5px;line-height:1.6;color:var(--muted)}
.bullets li::before{content:"";display:inline-block;width:3px;height:3px;background:var(--orange);margin-right:4px;vertical-align:middle}

/* title slide */
.cover .band{position:absolute;left:0;top:0;width:100%;height:200px;background:var(--orange)}
.cover .photo{left:0;top:0;width:118px;height:200px;clip-path:polygon(0 0,100% 0,70% 100%,0 100%)}
.cover h1{position:absolute;left:130px;top:58px;font-size:27px;line-height:1;color:var(--white)}
.cover .sub{position:absolute;left:130px;top:120px;font-size:7px;color:var(--white);letter-spacing:.6px}
.cover .date{position:absolute;left:130px;top:140px;font-size:5px;color:var(--orange-pale)}
.cover .brand{left:20px;bottom:32px;font-size:12px}

/* table of content */
.toc .side{position:absolute;left:0;top:0;width:140px;height:100%;background:var(--orange)}
.toc .side .photo{left:0;top:0;width:100%;height:110px;opacity:.5;clip-path:polygon(0 0,100% 0,100% 100%,0 60%)}
.toc h2{position:absolute;left:18px;top:120px;font-size:20px;line-height:1.05;color:var(--white)}
.toc .side .brand{left:18px;bottom:20px}
.toc ul{position:absolute;left:156px;right:16px;top:28px;list-style:none}
.toc li{display:flex;align-items:center;height:46px;border-bottom:1px solid #e4e0da;font-size:7px;font-weight:500;color:var(--ink);letter-spacing:.4px}
.toc li svg{width:12px;height:12px;margin-right:10px}
.toc li b{margin-left:auto;font-weight:500;color:var(--orange)}

/* title and content */
.tiles{position:absolute;left:18px;right:18px;top:110px;display:grid;grid-template-columns:repeat(4,1fr);gap:5px}
.tile{height:68px;padding:7px 5px;color:var(--white);font-size:4.5px;line-height:1.4;text-align:center}
.tile svg{width:14px;height:14px;display:block;margin:4px auto 5px}
.tile.t1{background:var(--orange)}.tile.t2{background:var(--orange-light)}.tile.t3{background:var(--tan)}.tile.t4{background:var(--grey)}

/* divider */
.divider{background:var(--cream)}
.divider .photo{right:0;top:0;width:250px;height:200px;clip-path:polygon(30% 0,100% 0,100% 100%,0 100%)}
.divider h2{position:absolute;left:22px;top:212px;font-size:17px;color:var(--orange)}
.divider .sub{position:absolute;left:22px;top:234px;font-size:5px;color:var(--muted);letter-spacing:.5px}
.divider .brand{left:22px;top:24px}
.divider.green{background:var(--sage)}
.divider.green .photo{width:100%;height:190px;clip-path:ellipse(95% 100% at 100% 0)}
.divider.green h2,.divider.green .sub{color:var(--white)}
.divider.green .brand{top:150px;color:var(--white)}

/* quote */
.quote{background:var(--cream)}
.quote blockquote{position:absolute;left:18px;right:30px;top:72px;font-family:"Roboto",Arial,sans-serif;font-weight:700;font-size:14.5px;line-height:1.28;color:var(--orange)}
.quote cite{position:absolute;left:18px;top:230px;font-style:normal;font-size:6px;color:var(--muted)}

/* thank you */
.thanks{background:var(--slate)}
.thanks .photo{left:0;top:0;width:100%;height:100%;opacity:.35}
.thanks h2{position:absolute;left:22px;top:110px;font-size:26px;line-height:1;color:var(--white)}
.thanks .brand{left:22px;bottom:22px}
.thanks .panel{position:absolute;right:0;top:0;width:170px;height:100%;background:rgba(60,62,58,.75);padding:40px 16px}
.thanks .panel .lead{font-size:7px;font-weight:700;color:var(--orange-pale);margin-bottom:2px}
.thanks .panel .copy{color:#d8d6cf;margin-bottom:22px}
.thanks .contact{list-style:none;font-size:6px;color:var(--white)}
.thanks .contact li{display:flex;align-items:center;gap:6px;margin-bottom:10px}
.thanks .contact svg{width:10px;height:10px}
</style>
</head>
<body>

<!-- ===== Featured slides ===== -->
<section class="slide cover" style="left:40px;top:250px">
  <div class="band"></div>
  <div class="photo photo-glass" role="img" aria-label="Glass facade of a modern building"></div>
  <h1 class="head">Presentation<br>Title Here</h1>
  <p class="sub head">Sub presentation title here</p>
  <p class="date">JUNE 2024</p>
  <span class="brand">STONEWAY</span>
</section>

<section class="slide toc" style="left:420px;top:250px">
  <div class="side">
    <div class="photo photo-glass" role="img" aria-label="Glass facade detail"></div>
    <h2 class="head">Table of<br>Content</h2>
    <span class="brand light">STONEWAY</span>
  </div>
  <ul>
    <li><svg viewBox="0 0 12 12"><circle cx="6" cy="4" r="2.5" fill="none" stroke="#d2622a"/><path d="M1.5 11c0-3 9-3 9 0" fill="none" stroke="#d2622a"/></svg>ABOUT US<b>01</b></li>
    <li><svg viewBox="0 0 12 12"><rect x="1" y="3" width="10" height="7" fill="none" stroke="#d2622a"/><path d="M4 3V1.5h4V3" fill="none" stroke="#d2622a"/></svg>OUR SERVICES<b>02</b></li>
    <li><svg viewBox="0 0 12 12"><circle cx="4" cy="4" r="2" fill="none" stroke="#d2622a"/><circle cx="8.5" cy="4.5" r="1.7" fill="none" stroke="#d2622a"/><path d="M0.5 11c0-3 7-3 7 0" fill="none" stroke="#d2622a"/></svg>OUR TEAM<b>03</b></li>
    <li><svg viewBox="0 0 12 12"><path d="M1 11V6h3v5M5 11V3h3v8M9 11V1h2v10" fill="none" stroke="#d2622a"/></svg>OUR BUSINESS<b>04</b></li>
    <li><svg viewBox="0 0 12 12"><rect x="1" y="2.5" width="10" height="7" fill="none" stroke="#d2622a"/><path d="M1 2.5l5 4 5-4" fill="none" stroke="#d2622a"/></svg>CONTACT<b>05</b></li>
  </ul>
</section>

<section class="slide divider" style="left:800px;top:250px">
  <div class="photo photo-interior" role="img" aria-label="Bright apartment living room interior"></div>
  <span class="brand">STONEWAY</span>
  <h2 class="head">Divider Title Slide</h2>
  <p class="sub head">Sub divider title</p>
</section>

<!-- ===== Left column ===== -->
<section class="slide cover" style="left:240px;top:848px">
  <div class="band"></div>
  <div class="photo photo-glass" role="img" aria-label="Glass facade of a modern building"></div>
  <h1 class="head">Presentation<br>Title Here</h1>
  <p class="sub head">Sub presentation title here</p>
  <p class="date">JUNE 2024</p>
  <span class="brand">STONEWAY</span>
</section>

<section class="slide toc" style="left:240px;top:1188px">
  <div class="side">
    <div class="photo photo-glass" role="img" aria-label="Glass facade detail"></div>
    <h2 class="head">Table of<br>Content</h2>
    <span class="brand light">STONEWAY</span>
  </div>
  <ul>
    <li><svg viewBox="0 0 12 12"><circle cx="6" cy="4" r="2.5" fill="none" stroke="#d2622a"/><path d="M1.5 11c0-3 9-3 9 0" fill="none" stroke="#d2622a"/></svg>ABOUT US<b>01</b></li>
    <li><svg viewBox="0 0 12 12"><rect x="1" y="3" width="10" height="7" fill="none" stroke="#d2622a"/><path d="M4 3V1.5h4V3" fill="none" stroke="#d2622a"/></svg>OUR SERVICES<b>02</b></li>
    <li><svg viewBox="0 0 12 12"><circle cx="4" cy="4" r="2" fill="none" stroke="#d2622a"/><circle cx="8.5" cy="4.5" r="1.7" fill="none" stroke="#d2622a"/><path d="M0.5 11c0-3 7-3 7 0" fill="none" stroke="#d2622a"/></svg>OUR TEAM<b>03</b></li>
    <li><svg viewBox="0 0 12 12"><path d="M1 11V6h3v5M5 11V3h3v8M9 11V1h2v10" fill="none" stroke="#d2622a"/></svg>OUR BUSINESS<b>04</b></li>
    <li><svg viewBox="0 0 12 12"><rect x="1" y="2.5" width="10" height="7" fill="none" stroke="#d2622a"/><path d="M1 2.5l5 4 5-4" fill="none" stroke="#d2622a"/></svg>CONTACT<b>05</b></li>
  </ul>
</section>

<section class="slide" style="left:240px;top:1528px">
  <h2 class="s-title head">Title and Content Sample</h2>
  <div style="position:absolute;left:18px;right:18px;top:40px">
    <p class="lorem-head">LOREM IPSUM</p>
    <ul class="bullets">
      <li>Lorem ipsum dolor sit amet, consectetur adipiscing elit sed do.</li>
      <li>Eiusmod tempor incididunt ut labore et dolore magna aliqua.</li>
      <li>Ut enim ad minim veniam quis nostrud exercitation.</li>
    </ul>
  </div>
  <div class="tiles">
    <div class="tile t1"><svg viewBox="0 0 14 14"><path d="M2 12V6l5-4 5 4v6z" fill="none" stroke="#fff"/></svg>Lorem ipsum dolor sit amet elit</div>
    <div class="tile t2"><svg viewBox="0 0 14 14"><rect x="2" y="4" width="10" height="8" fill="none" stroke="#fff"/><path d="M5 4V2h4v2" fill="none" stroke="#fff"/></svg>Sed do eiusmod tempor labore</div>
    <div class="tile t3"><svg viewBox="0 0 14 14"><circle cx="7" cy="7" r="5" fill="none" stroke="#fff"/><path d="M7 4v3l2 2" fill="none" stroke="#fff"/></svg>Ut enim ad minim veniam quis</div>
    <div class="tile t4"><svg viewBox="0 0 14 14"><path d="M2 12h10M3 12V7h2v5M6 12V4h2v8M9 12V2h2v10" fill="none" stroke="#fff"/></svg>Duis aute irure dolor in reprehen</div>
  </div>
  <div class="foot"><span class="brand">STONEWAY</span><small>Presentation title | 03</small></div>
</section>

<section class="slide" style="left:240px;top:1868px">
  <h2 class="s-title head">Title and Chart Content Sample</h2>
  <div style="position:absolute;left:18px;width:140px;top:44px">
    <p class="lorem-head">LOREM IPSUM</p>
    <p class="copy">Lorem ipsum dolor sit amet, consectetur adipiscing elit, sed do eiusmod tempor incididunt ut labore et dolore magna aliqua.</p>
    <ul class="bullets" style="margin-top:6px">
      <li>Ut enim ad minim veniam nostrud.</li>
      <li>Duis aute irure dolor in velit.</li>
      <li>Excepteur sint occaecat cupidatat.</li>
    </ul>
  </div>
  <svg style="position:absolute;left:170px;top:44px" width="172" height="190" viewBox="0 0 172 190">
    <text x="86" y="10" font-size="6" fill="#3a3a38" text-anchor="middle" font-family="Roboto,Arial,sans-serif">Sales Growth</text>
    <g stroke="#e6e2dc" stroke-width=".6">
      <line x1="18" y1="30" x2="168" y2="30"/><line x1="18" y1="65" x2="168" y2="65"/>
      <line x1="18" y1="100" x2="168" y2="100"/><line x1="18" y1="135" x2="168" y2="135"/>
    </g>
    <line x1="18" y1="170" x2="168" y2="170" stroke="#9a9a94" stroke-width=".8"/>
    <g fill="#d2622a">
      <rect x="26" y="120" width="9" height="50"/><rect x="63" y="95" width="9" height="75"/>
      <rect x="100" y="60" width="9" height="110"/><rect x="137" y="32" width="9" height="138"/>
    </g>
    <g fill="#e9925f">
      <rect x="36" y="138" width="9" height="32"/><rect x="73" y="112" width="9" height="58"/>
      <rect x="110" y="84" width="9" height="86"/><rect x="147" y="62" width="9" height="108"/>
    </g>
    <g fill="#75766f">
      <rect x="46" y="150" width="9" height="20"/><rect x="83" y="130" width="9" height="40"/>
      <rect x="120" y="108" width="9" height="62"/><rect x="157" y="90" width="9" height="80"/>
    </g>
    <g font-size="5" fill="#8b8b86" font-family="Roboto,Arial,sans-serif" text-anchor="middle">
      <text x="40" y="180">2021</text><text x="77" y="180">2022</text><text x="114" y="180">2023</text><text x="151" y="180">2024</text>
    </g>
  </svg>
  <div class="foot"><span class="brand">STONEWAY</span><small>Presentation title | 04</small></div>
</section>

<section class="slide" style="left:240px;top:2208px">
  <h2 class="s-title head">Two Content Sample</h2>
  <div style="position:absolute;left:18px;width:150px;top:44px">
    <p class="lorem-head">LOREM IPSUM</p>
    <p class="copy">Lorem ipsum dolor sit amet, consectetur adipiscing elit, sed do eiusmod tempor incididunt.</p>
    <ul class="bullets" style="margin-top:6px">
      <li>Ut enim ad minim veniam nostrud.</li>
      <li>Duis aute irure dolor in velit.</li>
    </ul>
    <p class="copy" style="margin-top:12px">Excepteur sint occaecat cupidatat non proident, sunt in culpa qui officia.</p>
  </div>
  <div style="position:absolute;left:190px;width:150px;top:44px">
    <p class="lorem-head">LOREM IPSUM</p>
    <p class="copy">Lorem ipsum dolor sit amet, consectetur adipiscing elit, sed do eiusmod tempor incididunt.</p>
    <ul class="bullets" style="margin-top:6px">
      <li>Ut enim ad minim veniam nostrud.</li>
      <li>Duis aute irure dolor in velit.</li>
    </ul>
    <p class="copy" style="margin-top:12px">Excepteur sint occaecat cupidatat non proident, sunt in culpa qui officia.</p>
  </div>
  <div class="foot"><span class="brand">STONEWAY</span><small>Presentation title | 05</small></div>
</section>

<section class="slide" style="left:240px;top:2548px">
  <h2 class="s-title head">Graphic Sample</h2>
  <svg style="position:absolute;left:0;top:40px" width="360" height="220" viewBox="0 0 360 220">
    <g transform="rotate(-90 180 110)" fill="none" stroke-width="20">
      <circle cx="180" cy="110" r="44" stroke="#d2622a" stroke-dasharray="43 233.5" stroke-dashoffset="0"/>
      <circle cx="180" cy="110" r="44" stroke="#75766f" stroke-dasharray="43 233.5" stroke-dashoffset="-46.1"/>
      <circle cx="180" cy="110" r="44" stroke="#e9925f" stroke-dasharray="43 233.5" stroke-dashoffset="-92.2"/>
      <circle cx="180" cy="110" r="44" stroke="#d2622a" stroke-dasharray="43 233.5" stroke-dashoffset="-138.3"/>
      <circle cx="180" cy="110" r="44" stroke="#75766f" stroke-dasharray="43 233.5" stroke-dashoffset="-184.4"/>
      <circle cx="180" cy="110" r="44" stroke="#e9925f" stroke-dasharray="43 233.5" stroke-dashoffset="-230.5"/>
    </g>
    <g font-family="Roboto Condensed,Arial Narrow,sans-serif" font-weight="700" font-size="6.5" fill="#d2622a">
      <text x="238" y="50">HEADING HERE</text><text x="258" y="112">HEADING HERE</text><text x="238" y="174">HEADING HERE</text>
      <text x="122" y="50" text-anchor="end">HEADING HERE</text><text x="102" y="112" text-anchor="end">HEADING HERE</text><text x="122" y="174" text-anchor="end">HEADING HERE</text>
    </g>
    <g font-family="Roboto,Arial,sans-serif" font-size="4.5" fill="#8b8b86">
      <text x="238" y="58">Lorem ipsum dolor sit amet</text><text x="258" y="120">Lorem ipsum dolor sit amet</text><text x="238" y="182">Lorem ipsum dolor sit amet</text>
      <text x="122" y="58" text-anchor="end">Lorem ipsum dolor sit amet</text><text x="102" y="120" text-anchor="end">Lorem ipsum dolor sit amet</text><text x="122" y="182" text-anchor="end">Lorem ipsum dolor sit amet</text>
    </g>
  </svg>
  <div class="foot"><span class="brand">STONEWAY</span><small>Presentation title | 06</small></div>
</section>

<!-- ===== Right column ===== -->
<section class="slide cover" style="left:620px;top:1060px">
  <div class="band"></div>
  <div class="photo photo-glass" role="img" aria-label="Glass facade of a modern building"></div>
  <h1 class="head">Presentation<br>Title Here</h1>
  <p class="sub head">Sub presentation title here</p>
  <p class="date">JUNE 2024</p>
  <span class="brand">STONEWAY</span>
</section>

<section class="slide divider" style="left:620px;top:1400px">
  <div class="photo photo-interior" role="img" aria-label="Bright apartment living room interior"></div>
  <span class="brand">STONEWAY</span>
  <h2 class="head">Divider Title Slide</h2>
  <p class="sub head">Sub divider title</p>
</section>

<section class="slide" style="left:620px;top:1740px">
  <h2 class="s-title head">Title and Image Content Sample</h2>
  <div style="position:absolute;left:18px;width:150px;top:44px">
    <p class="lorem-head">LOREM IPSUM</p>
    <p class="copy">Lorem ipsum dolor sit amet, consectetur adipiscing elit, sed do eiusmod tempor incididunt ut labore.</p>
    <ul class="bullets" style="margin-top:6px">
      <li>Ut enim ad minim veniam nostrud.</li>
      <li>Duis aute irure dolor in velit.</li>
      <li>Excepteur sint occaecat cupidatat.</li>
    </ul>
  </div>
  <div class="photo photo-building" style="left:182px;top:40px;width:160px;height:200px" role="img" aria-label="Residential apartment building with landscaped entrance"></div>
  <div class="foot"><span class="brand">STONEWAY</span><small>Presentation title | 07</small></div>
</section>

<section class="slide divider green" style="left:620px;top:2080px">
  <div class="photo photo-tower" role="img" aria-label="Modern apartment block exterior"></div>
  <span class="brand">STONEWAY</span>
  <h2 class="head">Divider Title Slide</h2>
  <p class="sub head">Sub divider title</p>
</section>

<section class="slide quote" style="left:620px;top:2420px">
  <h2 class="s-title head">Quote Sample Page</h2>
  <blockquote>Lorem Ipsum has been the industry's standard dummy text ever since the 1500s, when an unknown printer took a galley of type and scrambled it to make a type specimen book.</blockquote>
  <cite>John Doe</cite>
  <div class="foot"><span class="brand">STONEWAY</span><small>Presentation title | 09</small></div>
</section>

<section class="slide thanks" style="left:620px;top:2760px">
  <div class="photo photo-lobby" role="img" aria-label="Warm building lobby with timber panels"></div>
  <h2 class="head">Thank<br>You</h2>
  <span class="brand light">STONEWAY</span>
  <div class="panel">
    <p class="lead">LOREM IPSUM</p>
    <p class="copy">Lorem ipsum dolor sit amet, consectetur adipiscing elit sed do.</p>
    <ul class="contact">
      <li><svg viewBox="0 0 10 10"><path d="M2 1h2l1 2.5-1.3 1a5 5 0 0 0 2 2l1-1.3L9 6v2c0 .6-.4 1-1 1A8 8 0 0 1 1 2c0-.6.4-1 1-1z" fill="#f4c4a3"/></svg>+1 555 014 2800</li>
      <li><svg viewBox="0 0 10 10"><rect x="1" y="2" width="8" height="6" fill="none" stroke="#f4c4a3"/><path d="M1 2l4 3 4-3" fill="none" stroke="#f4c4a3"/></svg>hello@stoneway.example</li>
      <li><svg viewBox="0 0 10 10"><path d="M5 9S2 5.6 2 3.8a3 3 0 0 1 6 0C8 5.6 5 9 5 9z" fill="#f4c4a3"/><circle cx="5" cy="3.8" r="1" fill="#62655f"/></svg>12 Harbour Lane, Eastport</li>
      <li><svg viewBox="0 0 10 10"><circle cx="5" cy="5" r="4" fill="none" stroke="#f4c4a3"/><path d="M1 5h8M5 1c-2 2.5-2 5.5 0 8M5 1c2 2.5 2 5.5 0 8" fill="none" stroke="#f4c4a3"/></svg>www.stoneway.example</li>
    </ul>
  </div>
</section>

</body>
</html>
```